Glenvora pond linings website template

We need a template for our new website. Glenvora is currently marketed through www.sheetvale.com.au, and we are moving the pond/dam linings to a dedicated site www.glenvora.com.au

The site is essentially brochureware. The content (less landing page & photo gallery) is on the new site to give you a better idea of what we do. We are also on Facebook.com/glenvora

We are looking for a template/style which we can adapt to the different sections of the site as required. We also get a lot of phone/tablet visitors so an alternative mobile layout would be a bonus, but by no means required.

I am proficient in HTML/CSS & javascript so can code most designs thrown at me.

Any icons or interface fonts should be freely available web fonts where possible.

Target Market(s)

We are targeting both landscape professionals (design & construction) as well as the DIY market for ponds/wateragrdens.

Industry/Entity Type

Moving

Requirements
Must have
• We need a design (preferably layered PSD or AI) as basis for our overall site look and feel. Fonts/iconography/layout are where we are lacking. We can do the HTML/CSS/JS/PHP internally.
Nice to have
• A style guide either in file or separate would be nice.
Layers with effect (i.e.. :hover, CSS3 transition endpoints, etc)

```html
<!DOCTYPE html>
<html lang="en">
<head>
<meta charset="utf-8">
<title>Glenvora – Installation</title>
<link href="https://fonts.googleapis.com/css2?family=Open+Sans:wght@400;600;700;800&display=swap" rel="stylesheet">
<style>
:root{
  --bg:#e6e7e8;
  --navy:#0f3a6e;
  --green:#6b9b2b;
  --lime:#c6da3a;
  --orange:#f5821f;
  --text:#1d1d1d;
  --white:#ffffff;
}
*{margin:0;padding:0;box-sizing:border-box}
html,body{width:794px;height:1200px;overflow:hidden}
body{background:var(--bg);font-family:'Open Sans',Arial,sans-serif;color:var(--text);position:relative}
.page{position:absolute;inset:0}
.logo{position:absolute;left:123px;top:22px;display:flex;align-items:center;gap:6px;font-weight:700;font-size:20px;letter-spacing:1px;color:var(--navy);white-space:nowrap}
.logo-mark{width:22px;height:22px;background:var(--green)}
.social{position:absolute;display:flex;gap:2px}
.social span{width:18px;height:18px;display:block}
.social span:nth-child(1){background:var(--green)}
.social span:nth-child(2){background:var(--lime)}
.social span:nth-child(3){background:var(--green)}
.social.top{left:483px;top:29px}
.search{position:absolute;left:550px;top:29px;width:119px;height:18px;border:1px solid var(--green);background:var(--white);display:flex}
.search-field{flex:1;font-size:6px;color:#8aa0a8;padding:5px 6px;letter-spacing:.3px;white-space:nowrap}
.search-btn{width:21px;background:var(--green);display:flex;align-items:center;justify-content:center}
.nav{position:absolute;left:124px;top:66px;width:545px;height:29px;background:var(--navy);display:flex;padding-left:7px;overflow:hidden}
.nav a{flex:none;white-space:nowrap;color:var(--white);text-decoration:none;font-size:8.2px;font-weight:600;padding:0 8px;line-height:29px}
.nav a.active{background:var(--lime);color:var(--navy);padding:0 11px}
.main-title{position:absolute;left:123px;top:124px;width:378px;display:flex;align-items:center;gap:6px;font-size:15.5px;font-weight:800;color:var(--navy);white-space:nowrap}
.main-title::after{content:"";flex:1;height:2px;background:var(--navy);opacity:.7;margin-top:2px}
.intro{position:absolute;left:123px;top:153px;width:380px;font-size:8px;line-height:11px}
.intro p+p{margin-top:11px}
.card{position:absolute;left:124px;width:377px;height:129px;display:flex}
.card-photo{width:218px;height:100%}
.card-body{position:relative;flex:1;background:var(--green);color:var(--white);padding:18px 14px 0 18px}
.card-body h2{font-size:9.6px;font-weight:700;margin-bottom:5px;letter-spacing:.2px;white-space:nowrap}
.card-body p{font-size:7px;line-height:12px}
.learn{position:absolute;right:-4px;bottom:0;width:68px;height:17px;background:var(--orange);color:var(--white);font-size:8px;line-height:17px;text-align:center;white-space:nowrap;clip-path:polygon(8px 0,100% 0,100% 100%,0 100%)}
.about{position:absolute;left:520px;top:126px;width:149px;height:212px;background:linear-gradient(160deg,#6f7f5c,#3d4a36 55%,#2a3324);color:var(--white);padding:18px 14px}
.about h3{font-size:15px;font-weight:800;padding-bottom:4px;border-bottom:2px solid var(--white);margin-bottom:6px;white-space:nowrap}
.about p{font-size:7.6px;line-height:9.5px}
.about a{display:block;margin-top:6px;color:var(--orange);font-size:7.6px;text-decoration:none}
.map{position:absolute;left:520px;top:357px;width:149px;height:93px;background:linear-gradient(135deg,#eef0e4,#e5e7d8 60%,#f0d9a8)}
.view{position:absolute;left:624px;top:449px;font-size:7px;color:var(--orange);white-space:nowrap}
.call{position:absolute;left:522px;top:461px;display:flex;align-items:center;gap:4px}
.call-tag{background:var(--navy);color:var(--white);font-size:6.5px;padding:1px 14px 1px 8px;white-space:nowrap;clip-path:polygon(0 0,100% 0,88% 50%,100% 100%,0 100%)}
.phone{position:absolute;left:522px;top:476px;font-size:15px;color:var(--navy);white-space:nowrap}
.footer-rule{position:absolute;left:124px;top:1127px;width:545px;height:2px;background:var(--white)}
.footer-links{position:absolute;left:123px;top:1152px;font-size:6.4px;line-height:8.5px;color:var(--text);white-space:nowrap}
.footer-links span{margin:0 3px}
.social.bottom{left:610px;top:1150px}
</style>
</head>
<body>
<div class="page">
  <div class="logo"><span class="logo-mark"></span>GLENVORA</div>
  <div class="social top"><span></span><span></span><span></span></div>
  <div class="search">
    <div class="search-field">SEARCH</div>
    <div class="search-btn"><svg width="8" height="8" viewBox="0 0 10 10"><circle cx="4" cy="4" r="3" fill="none" stroke="#fff" stroke-width="1.5"/><line x1="6.2" y1="6.2" x2="9" y2="9" stroke="#fff" stroke-width="1.6"/></svg></div>
  </div>
  <nav class="nav">
    <a>HOME</a><a>ABOUT US</a><a>HAPPENINGS</a><a>GALLERY</a><a>LINER STYLES</a><a>PREPARATION</a><a class="active">INSTALLATION</a><a>CONTACT US</a>
  </nav>

  <h1 class="main-title">INSTALLATION</h1>
  <div class="intro">
    <p>Installing your Glenvora pond liner is an easy task, unfortunately there is no one single correct way to install it. Installation methods vary between each type of liner and the finish you are trying to achieve. The only constant between all installation methods is that the edge must be physically held down in one way or another such as using rocks, burying in a ditch or covering with a capping stone.</p>
    <p>In this section we detail some common installation methods as well as tips and tricks we have discovered over the years.</p>
  </div>

  <div class="card" style="top:238px">
    <div class="card-photo" role="img" aria-label="Workers laying a black liner sheet across a dug pond site" style="background:linear-gradient(160deg,#8a7a5a,#4a4a48 45%,#2b2c2e)"></div>
    <div class="card-body"><h2>Standard Installation</h2><p>Step One. Carefully lay out the shape of your pond with a rope or hose. Start digging, always cut into the shape. Dig to a minimum depth of 350mm, leaving 225mm wide shelves 225mm below the water level...</p><span class="learn">Learn More</span></div>
  </div>
  <div class="card" style="top:381px">
    <div class="card-photo" role="img" aria-label="Square formal pond lined with folded black liner corners" style="background:linear-gradient(180deg,#3a3a3a,#1f1f20 70%,#cfd0cc)"></div>
    <div class="card-body"><h2>Folding Corners</h2><p>When you build a formal water garden with vertical sides, you have two choices for installation, either a profile liner or a flat sheet with folded corners. The “Folded Corner” installation method is our preferred...</p><span class="learn">Learn More</span></div>
  </div>
  <div class="card" style="top:525px">
    <div class="card-photo" role="img" aria-label="Black liner with pipe penetrations beneath a metal grate" style="background:linear-gradient(180deg,#6a6d70,#2c2e30 35%,#242527)"></div>
    <div class="card-body"><h2>Pipes &amp; Penetrations</h2><p>Penetrations are an unfortunate requirement of most ponds. Penetrations can be required for filling systems, balancing, pumping and overflows amongst other reasons. These penetrations...</p><span class="learn">Learn More</span></div>
  </div>
  <div class="card" style="top:671px">
    <div class="card-photo" role="img" aria-label="Garden pond edge with timber decking and flowering plants" style="background:linear-gradient(150deg,#6e6a5c,#55606a 50%,#5a5a7a)"></div>
    <div class="card-body"><h2>Edge Finishing</h2><p>There are almost as many ways to finish your pond edge as there are ways to build your pond. Here we detail some of the most common methods. Capping Block Finish In formal installations</p><span class="learn">Learn More</span></div>
  </div>
  <div class="card" style="top:819px">
    <div class="card-photo" role="img" aria-label="Small waterfall flowing over river pebbles and rocks" style="background:linear-gradient(160deg,#8a8a80,#5a5e58 50%,#a89e90)"></div>
    <div class="card-body"><h2>Waterfalls</h2><p>Streams and waterfalls can be incorporated into a pond design very simply with Glenvora pond liners. Where the connection between the pond and the waterfall is above the level of the still water, you simply...</p><span class="learn">Learn More</span></div>
  </div>
  <div class="card" style="top:966px">
    <div class="card-photo" role="img" aria-label="Koi and goldfish swimming over pebbles in clear water" style="background:linear-gradient(150deg,#7a5a38,#5a4630 50%,#8a6a48)"></div>
    <div class="card-body"><h2>Water, Plants &amp; Fish</h2><p>Before the addition of your fish it is important to stabilize the water. This can be achieved with a few easy steps. Clean out your pond before the addition of water. Remove all dirt and other contaminants</p><span class="learn">Learn More</span></div>
  </div>

  <aside class="about" role="img" aria-label="About us panel over a photo of a garden pond">
    <h3>ABOUT US</h3>
    <p>Lorem ipsum dolor sit amet, consectetur adipisicing elit, sed do eiusmod tempor incididunt ut labore et dolore magna aliqua. Ut enim ad minim veniam, quis nostrud exercitation ullamco laboris nisi ut aliquip ex ea commodo consequat. Duis aute irure dolor in reprehenderit in voluptate velit esse cillum dolore eu fugiat nulla pariatur. Excepteur sint occaecat cupidatat non</p>
    <a>Read More</a>
  </aside>
  <div class="map" role="img" aria-label="Location map of the business area"></div>
  <div class="view">View Enlarge</div>
  <div class="call">
    <svg width="8" height="9" viewBox="0 0 10 10"><path d="M2 1 L4 1 L4.5 3.5 L3.3 4.3 Q4.2 6.2 5.8 6.8 L6.6 5.6 L9 6.2 L9 8.2 Q4 9 1.5 3 Z" fill="#0f3a6e"/></svg>
    <span class="call-tag">CALL US</span>
  </div>
  <div class="phone">8200 - 316 - 574</div>

  <div class="footer-rule"></div>
  <div class="footer-links">
    Home<span>|</span>About Us<span>|</span>Happenings<span>|</span>Gallery<span>|</span>Liner Styles<span>|</span>Preparation<span>|</span>Installation<span>|</span>Contact Us<br>
    Copyright © 2013 - Terms and Conditions - Designed by www.studiofernwick.com
  </div>
  <div class="social bottom"><span></span><span></span><span></span></div>
</div>
</body>
</html>
```